Law firm needs stationary and envelope design*

We would like to incorporate our logo into letterhead design and envelopes. We are looking for something that is moderately conservative but not old law firm style. Both the envelopes and the letterhead must have both firm addresses. We would like to incorporate the color of the logo, but only a small amount of color - perhaps on one of the borders. The addresses for the firm locations are listed below. Given that it is a law firm, it needs to somewhat conservative, but not the old school, small black font on cream colored paper design.

The firm addresses are:

27815 N. Harlow Pemberton Pkwy.
Ste 740
Scottsdale, AZ 85419

6208 E. Juniper Street
Ste 820
Burbank, CA 91873

Legal

Designer to choose colors to be used in the design.

• Both addresses:
• 27815 N. Harlow Pemberton Pkwy.
• Ste 740
• Scottsdale, AZ 85419
• 6208 E. Juniper Street
• Ste 820
• Burbank, CA 91873
• Small amount of color on border(s) that matches the logo but not too much color

```html
<!DOCTYPE html>
<html lang="en">
<head>
<meta charset="utf-8">
<title>Brennick Law — Letterhead Header</title>
<link rel="stylesheet" href="https://fonts.googleapis.com/css2?family=Cinzel:wght@400;500&display=swap">
<style>
  :root {
    --paper: #ffffff;
    --navy: #2d2a6e;
    --ink: #23223a;
    --accent-red: #e2404f;
    --rule-violet: #8a6aa6;
  }
  html, body {
    margin: 0;
    padding: 0;
    overflow: hidden;
    background: var(--paper);
  }
  .canvas {
    position: relative;
    width: 1200px;
    height: 720px;
    background: var(--paper);
    overflow: hidden;
  }
  .brand-mark {
    position: absolute;
    left: 354px;
    top: 300px;
    width: 64px;
    height: 64px;
    border-radius: 50%;
    background: var(--navy);
  }
  .divider {
    position: absolute;
    left: 482px;
    top: 257px;
    width: 3px;
    height: 166px;
    background: var(--accent-red);
  }
  .firm-block {
    position: absolute;
    left: 512px;
    top: 278px;
    width: 380px;
  }
  .firm-name {
    margin: 0;
    font-family: "Cinzel", serif;
    font-weight: 400;
    font-size: 46px;
    line-height: 50px;
    letter-spacing: 0.5px;
    color: var(--navy);
    white-space: nowrap;
  }
  .name-rule {
    width: 363px;
    height: 1px;
    background: var(--rule-violet);
    margin-top: -1px;
  }
  .office {
    margin: 0;
    font-family: "Cinzel", serif;
    font-style: normal;
    font-weight: 500;
    font-size: 15px;
    line-height: 16.5px;
    color: var(--ink);
    white-space: nowrap;
  }
  .office--primary { margin-top: 6px; }
  .office--secondary { margin-top: 16px; }
</style>
</head>
<body>
  <div class="canvas">
    <div class="brand-mark" aria-hidden="true"></div>
    <div class="divider" aria-hidden="true"></div>
    <div class="firm-block">
      <h1 class="firm-name">BRENNICK LAW</h1>
      <div class="name-rule" aria-hidden="true"></div>
      <address class="office office--primary">
        27815 N. Harlow Pemberton Pkwy. Ste 740<br>
        Scottsdale, AZ 85419
      </address>
      <address class="office office--secondary">
        6208 E. Juniper Street<br>
        Ste 820
      </address>
    </div>
  </div>
</body>
</html>
```